Party Invitation for Newly Weds

We would like a A5 flyer-style invite in a file suitable for both hard-copy print and web-publishing. It should be designed in the style of a 1950's American Diner Menu incorporating the colours: Ivory, Crimson, Black, and possibly period Green.

We think using the shape of a 50's Juke Box could be a good platform for the design although we are very open to other ideas. We require the design to include the following features:

1. A tattoo-style heart with scroll banner containing our names - TED & LUCY

2. Main Heading - "Wedlock Wing-Ding & Nuptial Knees Up"

3. Feature Headings with icons - DRINK (with cocktail glasses), DANCE (with twisting silhouettes), DEVOUR (with burger & fries)

4. Sub Headings as Menu Items with descriptions as follows:

a. Hey Cat, When's It At?
Venue Doors @ 7pm
Bride & Groom Arrive @ 7.30pm
Be there or be sQuare!

b. Where To Go, Daddy-O!
The Millpond
7, Brackwell Lane
Leeds, LS2 9QT

c. What's Cookin', Man?
DJs & Dancing all night from 7pm
Food Served on the terrace from 8pm
Late Bar from til 2am

d. Ya need digs? Dig this...
Special Rate for Party Guests at Marlow Quayside
£79 Bed & Breakfast
Limited Numbers - Book Early
Call (0113) 2987654 and quote 'PEXOR'

e. If You Want To Share Your Good Vibes...
Your presence, your love and your laughter will be a real neat-o gift for us to cherish, but should you want to splash the cash and spread your love we would be MADE UP with a small donation towards our American Road Trip Honeymoon!!

f. Please R.S.V.P by July 1st.

g. Strictly Over 18's Only

Industry/Entity Type

Publishing

Colors
87cfc6
f04b51
fefdec
1b1b1b

Requirements
Must have
• see project description
• genuine late 50's/early 60's retro style
• classic fonts
Nice to have
• asymmetric shapes
• personal touches
Should not have
• over dependence on food imagery - this is a menu-style design, not an actual menu!

```html
<!DOCTYPE html>
<html lang="en">
<head>
<meta charset="utf-8">
<title>Wedlock Wing-Ding &amp; Nuptial Knees Up — Ted &amp; Lucy</title>
<link rel="stylesheet" href="https://fonts.googleapis.com/css2?family=Lobster&family=Lobster+Two:ital,wght@1,400;1,700&family=Quicksand:wght@400;500;600&display=swap">
<style>
  :root{
    --crimson:#f04b51;
    --aqua:#87cfc6;
    --ivory:#fefdec;
    --ink:#1b1b1b;
    --rose:#e8404a;
  }
  *{box-sizing:border-box;margin:0;padding:0}
  html,body{width:849px;height:1200px;overflow:hidden;background:var(--ivory)}
  .invite{
    position:relative;width:849px;height:1200px;overflow:hidden;
    background:repeating-linear-gradient(90deg,
      var(--crimson) 0 18px, var(--ivory) 18px 24px,
      var(--aqua) 24px 31px, var(--ivory) 31px 37px);
    font-family:"Quicksand",sans-serif;color:var(--ink);
  }
  .jukebox{position:absolute;inset:0}
  .heart-art{
    position:absolute;left:305px;top:120px;width:240px;height:200px;
    background:radial-gradient(circle at 50% 40%,#f4636a,var(--crimson) 70%);
    border:4px solid var(--ink);border-radius:48% 48% 50% 50% / 40% 40% 60% 60%;
  }
  .names-banner{
    position:absolute;left:290px;top:188px;width:270px;height:46px;
    background:var(--aqua);border:3px solid var(--ink);border-radius:6px;
    transform:rotate(-7deg);
    display:flex;align-items:center;justify-content:center;
    font-family:"Lobster Two",cursive;font-style:italic;font-weight:700;font-size:30px;color:var(--ink);
  }
  .title-plate{
    position:absolute;left:132px;top:318px;width:585px;height:118px;
    background:var(--crimson);border:5px solid var(--aqua);
    box-shadow:0 0 0 5px var(--ivory),0 0 0 8px var(--aqua);
    border-radius:14px;text-align:center;color:var(--ivory);
    font-family:"Lobster",cursive;font-size:38px;line-height:46px;padding-top:12px;
  }
  .features{position:absolute;left:150px;top:506px;width:550px;display:flex;justify-content:space-between}
  .feature{width:170px;text-align:center}
  .feature h2{font-family:"Lobster Two",cursive;font-style:italic;font-weight:700;font-size:40px;color:var(--crimson);line-height:50px}
  .feature .icon{display:block;margin:8px auto 0;width:96px;height:118px;border-radius:10px;background:linear-gradient(180deg,#f25d62,var(--crimson))}
  .details{
    position:absolute;left:124px;top:680px;width:602px;height:300px;
    border:3px solid var(--aqua);display:grid;grid-template-columns:1fr 1fr;
  }
  .details section{text-align:center;padding:22px 14px 0}
  .details section+section{border-left:3px solid var(--aqua)}
  .menu-item{margin-bottom:26px}
  .menu-item h3,.vibes h3{font-family:"Lobster Two",cursive;font-style:italic;font-weight:700;font-size:23px;color:var(--crimson);margin-bottom:8px}
  .menu-item p,.vibes p{font-size:14.5px;line-height:20px;font-weight:500}
  .accent{color:var(--crimson)}
  .small{font-size:11.5px!important;line-height:15px!important}
  .vibes{position:absolute;left:124px;top:994px;width:602px;height:118px;border:3px solid var(--aqua);border-top:none;text-align:center;padding:10px 26px 0}
  .vibes p{text-align:left;font-size:13.5px;line-height:18px}
  .footer-band{
    position:absolute;left:118px;top:1118px;width:614px;height:56px;
    display:flex;justify-content:space-between;align-items:center;padding:0 46px;
    font-size:14.5px;font-weight:500;
  }
</style>
</head>
<body>
<main class="invite">
  <svg class="jukebox" width="849" height="1200" viewBox="0 0 849 1200" aria-hidden="true">
    <path d="M92 310 V250 Q92 20 425 12 Q758 20 758 250 V310 Z" fill="var(--ivory)" stroke="var(--aqua)" stroke-width="6"/>
    <path d="M112 310 V255 Q112 38 425 30 Q738 38 738 255 V310" fill="none" stroke="var(--aqua)" stroke-width="3"/>
    <rect x="40" y="300" width="770" height="72" rx="4" fill="var(--ivory)" stroke="var(--aqua)" stroke-width="5"/>
    <rect x="70" y="286" width="710" height="100" rx="4" fill="var(--ivory)" stroke="var(--aqua)" stroke-width="5"/>
    <rect x="92" y="300" width="666" height="830" fill="var(--ivory)" stroke="var(--aqua)" stroke-width="6"/>
    <rect x="106" y="456" width="638" height="664" fill="none" stroke="var(--aqua)" stroke-width="3"/>
    <rect x="112" y="1112" width="626" height="68" fill="var(--ivory)" stroke="var(--aqua)" stroke-width="5"/>
    <circle cx="425" cy="1146" r="44" fill="var(--ivory)" stroke="var(--aqua)" stroke-width="14"/>
  </svg>

  <div class="heart-art" role="img" aria-label="Tattoo-style heart illustration with rays behind it"></div>
  <div class="names-banner">Ted &amp; Lucy</div>

  <h1 class="title-plate">Wedlock Wing-Ding<br>&amp; Nuptial Knees Up</h1>

  <div class="features">
    <div class="feature"><h2>Drink</h2><span class="icon" role="img" aria-label="Cocktail glass illustration"></span></div>
    <div class="feature"><h2>Dance</h2><span class="icon" role="img" aria-label="Twisting dancing couple silhouette"></span></div>
    <div class="feature"><h2>Devour</h2><span class="icon" role="img" aria-label="Burger and fries illustration"></span></div>
  </div>

  <div class="details">
    <section>
      <div class="menu-item">
        <h3>Hey Cat, When's It At?</h3>
        <p>Venue Doors @ 7pm<br>Bride &amp; Groom Arrive @ 7.30pm<br><span class="accent">Be there or be sQuare!</span></p>
      </div>
      <div class="menu-item">
        <h3>What's Cookin', Man?</h3>
        <p>DJs &amp; Dancing all night from 7pm<br>Food Served on the terrace from 8pm<br>Late Bar from til 2am</p>
      </div>
    </section>
    <section>
      <div class="menu-item">
        <h3>Where To Go, Daddy-O!</h3>
        <p>The Millpond<br>7, Brackwell Lane<br>Leeds, LS2 9QT</p>
      </div>
      <div class="menu-item">
        <h3>Ya need digs? Dig this...</h3>
        <p class="small">Special Rate for Party Guests at Marlow Quayside</p>
        <p><span class="accent">£79 Bed &amp; Breakfast</span><br>Limited Numbers - Book Early<br>Call (0113) 2987654 and quote 'PEXOR'</p>
      </div>
    </section>
  </div>

  <div class="vibes">
    <h3>If You Want To Share Your Good Vibes...</h3>
    <p>Your presence, your love and your laughter will be a real neat-o gift for us to cherish, but should you want to splash the cash and spread your love we would be MADE UP with a small donation towards our American Road Trip Honeymoon!!</p>
  </div>

  <footer class="footer-band">
    <span>Please R.S.V.P by July 1st.</span>
    <span>Strictly Over 18's Only</span>
  </footer>
</main>
</body>
</html>
```